Website redesign for Halt and reBloom

We would like to update the design of our current website to a more concise, conversion optimized design.
The goal of our website is to get our message across as concisely as possible plus encourage people to contact us for more information or to book a consultation.
We need a redesign of the home page and 1 internal page - just for design/layout purposes/format purposes.

Target Market(s)

Males 20-45 years old who are concerned about hair loss and who want to regrow their own hair.

Industry/Entity Type

Health And Wellness

Number of Pages Required

2 page

Font styles to use
Sans Serif

Colors
00a990
33a6d7
ffffff
9d9d9d

Requirements
Must have
• We want the home page to be very concise and to the point in getting the message across. We want to get across the following 6 key messages:
• 1. Dr Quimby story – why he created this solution
• 2. Hair loss is caused by a chemical imbalance
• 3. Halt and rebloom conducts genetic and DNA analysis, then rebalances body chemistry, thus reversing the hair loss process and enabling your own hair to regrow naturally
• 4. Money back guaranteed results
• 5. Only The Active ingredients – no harsh preservatives or chemicals are included
• 6. All ingredients are FDA approved and safe – no side effects
• We also need a strong call to action. We want people to call or email us to find out more information or to schedule a consultation.
• Here is our current website which is not performing as we would hope: http://www.haltandrebloom-example.com/
• Here is our press release for further information: https://www.pressdeskly-example.com/news/finally-we-now-have-a-cure-for-male-pattern-baldness-19187647
• I uploaded the logo files, but let me know if anything else is needed and I can add it.

```html
<!DOCTYPE html>
<html lang="en">
<head>
<meta charset="utf-8">
<title>Halt &amp; reBloom — Home</title>
<link rel="stylesheet" href="https://fonts.googleapis.com/css2?family=Quicksand:wght@300;400;500;600;700&display=swap">
<style>
  :root{
    --teal:#00a990;
    --blue:#33a6d7;
    --white:#ffffff;
    --grey:#9d9d9d;
    --text:#555555;
    --dark:#1a1a1a;
    --rule:#d9d9d9;
  }
  *{margin:0;padding:0;box-sizing:border-box}
  html,body{width:1200px;height:1199px;overflow:hidden;background:var(--white)}
  body{position:relative;font-family:"Quicksand",sans-serif;color:var(--text)}
  .abs{position:absolute}

  .site-header{left:0;top:0;width:1200px;height:58px;background:var(--white)}
  .brand{left:190px;top:15px;display:flex;align-items:center;gap:8px}
  .brand-mark{width:24px;height:24px;border-radius:50%;background:var(--teal)}
  .brand-name{font-size:18px;font-weight:500;color:var(--grey);line-height:1}
  .main-nav{left:410px;top:19px;display:flex;gap:18px;font-size:10px;font-weight:500;letter-spacing:.2px;color:#888}
  .main-nav .active{color:var(--blue);font-weight:700}

  .hero{left:0;top:58px;width:1200px;height:459px;
    background:linear-gradient(90deg,#e9e7e4 0%,#f2f1ee 35%,#ece9e5 60%,#ddd7d0 100%)}
  .hero-photo{left:560px;top:58px;width:560px;height:409px;
    background:radial-gradient(ellipse at 55% 60%,#efeedd 0%,#e4dcc9 45%,rgba(230,225,215,0) 75%)}
  .hero-title{left:229px;top:184px;font-size:35px;font-weight:500;color:var(--dark)}
  .hero-sub{left:229px;top:234px;font-size:22px;font-weight:500;color:var(--teal);line-height:27px}

  .appointment{left:158px;top:467px;width:885px;height:210px;background:var(--teal);border-bottom:6px solid #9a9a9a;color:var(--white)}
  .appt-ask{left:22px;top:16px;font-size:22px;font-weight:400;display:flex;align-items:center;gap:5px}
  .appt-ask svg{width:13px;height:15px}
  .appt-head{left:58px;top:52px;font-size:26px;font-weight:700;letter-spacing:.3px}
  .appt-btn{left:129px;top:111px;width:215px;height:28px;border:1.5px solid var(--white);border-radius:14px;font-size:15px;font-weight:400;display:flex;align-items:center;justify-content:center}
  .hours-title{left:572px;top:53px;font-size:16px;font-weight:700;display:flex;align-items:center;gap:8px}
  .hours{left:572px;top:96px;width:222px;font-size:11px;font-weight:600}
  .hours-row{display:flex;height:31px;align-items:center;border-bottom:1px solid var(--white)}
  .hours-row span:nth-child(1){width:108px}
  .hours-row span:nth-child(2){width:27px}
  .hours-row span:nth-child(3){width:43px}
  .hours-row span:nth-child(4){width:16px}

  .welcome{left:0;top:733px;width:1200px;text-align:center;color:var(--grey)}
  .welcome h1{font-size:37px;font-weight:500}
  .welcome p{font-size:15px;font-weight:300;margin-top:4px}

  .section-title{font-size:22px;font-weight:500;color:#4a4a4a}
  .section-sub{font-size:14px;font-weight:500;color:#3a3a3a;line-height:21px}
  .section-body{font-size:10.5px;font-weight:400;color:#666;line-height:21px;width:510px}
  .story-title{left:189px;top:851px}
  .story-sub{left:188px;top:886px}
  .story-body{left:190px;top:944px}
  .divider{left:193px;top:1080px;width:482px;height:1px;background:var(--rule)}
  .how-title{left:194px;top:1112px}
  .how-sub{left:189px;top:1150px}
  .how-body{left:189px;top:1184px;width:530px}
  .doctor-photo{left:736px;top:866px;width:264px;height:306px;
    background:linear-gradient(180deg,#f4f4f4 0%,#e6ddd4 35%,#3fb8bd 60%,#2aa5ab 100%);border-radius:110px 110px 6px 6px}
</style>
</head>
<body>
  <header class="site-header abs">
    <div class="brand abs">
      <span class="brand-mark"></span>
      <span class="brand-name">Crownwell Clinic</span>
    </div>
    <nav class="main-nav abs">
      <span class="active">HOME</span><span>ABOUT US</span><span>HOW IT WORKS</span><span>SUCCESS STORIES</span><span>FAQS</span><span>BLOG</span><span>SALON PARTNERS</span><span>BOOK NOW</span><span>CONTACT</span>
    </nav>
  </header>

  <section class="hero abs"></section>
  <div class="hero-photo abs" role="img" aria-label="Smiling young man combing his full head of hair"></div>
  <h2 class="hero-title abs">Are you a candidate?</h2>
  <p class="hero-sub abs">Stop Hereditary Hair Loss<br>And Regrow a Full,<br>Healthy Head of Hair</p>

  <section class="appointment abs">
    <div class="appt-ask abs">
      <svg viewBox="0 0 13 15" fill="none" stroke="#fff" stroke-width="1.2"><rect x="2" y="1" width="9" height="13" rx="1"/><line x1="0.5" y1="4" x2="3" y2="4"/><line x1="0.5" y1="7.5" x2="3" y2="7.5"/><line x1="0.5" y1="11" x2="3" y2="11"/></svg>
      Need a personalized consultation?
    </div>
    <div class="appt-head abs">JUST MAKE AN APPOINTMENT</div>
    <div class="appt-btn abs">GET AN APPOINTMENT</div>
    <div class="hours-title abs">
      <svg width="11" height="11" viewBox="0 0 11 11" fill="none" stroke="#fff" stroke-width="1"><circle cx="5.5" cy="5.5" r="4.8"/><path d="M5.5 2.8v2.9h2"/></svg>
      WORKING TIME
    </div>
    <div class="hours abs">
      <div class="hours-row"><span>Monday - Friday</span><span>-</span><span>09:00</span><span>-</span><span>17:00</span></div>
      <div class="hours-row"><span>Saturday</span><span>-</span><span>08:00</span><span>-</span><span>14:00</span></div>
    </div>
  </section>

  <section class="welcome abs">
    <h1>Welcome to Halt &amp; reBloom™</h1>
    <p>The First Non-Surgical Hair Loss Solution With Clinically Proven Results</p>
  </section>

  <h3 class="section-title story-title abs">Dr. Quimby’ Story</h3>
  <p class="section-sub story-sub abs">The Revolutionary New Solution For Hair Loss That Uses Personalized Medicine.<br>To Stop Hair Loss and Regrow Your Thinning / Receding Hair.</p>
  <p class="section-body story-body abs">Dr. Robert Quimby, the creator of Halt and reBloom is a renowned hair restoration expert. After seeing first his father and then older brothers thin and go bald, he dedicated his life to finding the cure for hair loss. After initially pioneering the single hair method for hair transplant, he determined there must be a non-surgical solution and spent the last 20 years in research and clinical trial and error first creating, then perfecting what is now the Halt and reBloom solution for hair loss.</p>
  <div class="divider abs"></div>
  <h3 class="section-title how-title abs">How it Works</h3>
  <p class="section-sub how-sub abs">The science behind the effectiveness of Halt &amp; reBloom™</p>
  <p class="section-body how-body abs">Halt and reBloom uses a scientific approach to hair loss by treating your unique cause. Every case is different</p>
  <div class="doctor-photo abs" role="img" aria-label="Portrait of the doctor in teal scrubs with arms crossed"></div>
</body>
</html>
```